VORLA:advise Business Cards

We need a business card design for VORLA:advise (Logo Attached), a management consultancy specialized in brand & business building.

Design should be clean, smart and a touch of innnovation without being gimmicky.

The details on the card should be:
Name: Tomas Vellaquin
Title: Managing Director
Address: 42 Marden Wharf, Kestrel Tower Building, Singapore 073296
Tel: +6284729156048
email: tv@vorlaadvise.example
website: vorlaadvise.example

For further background on corporate identity, please check www.vorlaadvise.example
Updates

Dear all,

Many thanks for the submissions so far! I gave feedback to those designs that I prefer at this stage.

Overall I see that my preference goes into the direction that 'less is more' and 'simple is beautiful'

Please create uniqueness and standout by the simplicity and attraction of the overall concept and design.

Many thanks and please shout incase of questions!

Tomas

Industry/Entity Type

Business

```html
<!DOCTYPE html>
<html lang="en">
<head>
<meta charset="utf-8">
<title>VORLA:advise — Business Card, Tomas Vellaquin</title>
<link href="https://fonts.googleapis.com/css2?family=Alfa+Slab+One&family=Arimo:wght@700&family=Open+Sans:wght@800&display=swap" rel="stylesheet">
<style>
  :root {
    --paper: #ffffff;
    --ember-top: #9a2604;
    --ember-deep: #5c1404;
    --orange-mid: #e4620e;
    --orange-low: #f7a52a;
    --panel: #2b2b2c;
    --panel-edge: #1d1d1e;
    --ink: #000000;
    --logo-ink: #ffffff;
  }
  html, body {
    margin: 0;
    padding: 0;
    width: 1200px;
    height: 685px;
    overflow: hidden;
    background: var(--paper);
  }
  .card {
    position: absolute;
    left: 9px;
    top: 13px;
    width: 1183px;
    height: 655px;
    overflow: hidden;
    background:
      radial-gradient(ellipse 520px 340px at 100% 0%, var(--ember-deep) 0%, rgba(92,20,4,0) 100%),
      linear-gradient(180deg, var(--ember-top) 0%, #c8420a 22%, var(--orange-mid) 48%, #f08a1e 75%, var(--orange-low) 100%);
  }
  .brand-panel {
    position: absolute;
    left: 0;
    top: 113px;
    width: 525px;
    height: 263px;
    background: linear-gradient(180deg, var(--panel) 0%, var(--panel-edge) 100%);
    box-shadow: 4px 4px 6px rgba(0,0,0,0.55);
    display: flex;
    align-items: center;
    justify-content: center;
  }
  .brand-name {
    font-family: "Arimo", Arial, sans-serif;
    font-weight: 700;
    font-size: 64px;
    color: var(--logo-ink);
    letter-spacing: 1px;
  }
  .holder-name {
    position: absolute;
    left: 555px;
    top: 70px;
    margin: 0;
    font-family: "Alfa Slab One", Georgia, serif;
    font-weight: 400;
    font-size: 80px;
    line-height: 1;
    color: var(--ink);
    white-space: nowrap;
    transform: scale(0.66, 1.35);
    transform-origin: left top;
    text-shadow: 3px 4px 5px rgba(0,0,0,0.6);
  }
  .holder-title {
    position: absolute;
    left: 664px;
    top: 214px;
    margin: 0;
    font-family: "Open Sans", Verdana, sans-serif;
    font-weight: 800;
    font-size: 27px;
    color: var(--ink);
    text-shadow: 2px 2px 3px rgba(0,0,0,0.45);
  }
  .contact {
    position: absolute;
    left: 570px;
    margin: 0;
    color: var(--ink);
    white-space: nowrap;
    text-shadow: 2px 3px 4px rgba(0,0,0,0.5);
  }
  .contact-tel {
    top: 416px;
    font-family: "Open Sans", Verdana, sans-serif;
    font-weight: 800;
    font-size: 25px;
    letter-spacing: 2px;
  }
  .contact-email {
    top: 500px;
    font-family: "Arimo", Arial, sans-serif;
    font-weight: 700;
    font-size: 31px;
  }
  .contact-web {
    top: 566px;
    font-family: "Arimo", Arial, sans-serif;
    font-weight: 700;
    font-size: 37px;
    transform: scaleX(0.9);
    transform-origin: left top;
  }
</style>
</head>
<body>
  <main class="card">
    <div class="brand-panel">
      <span class="brand-name">VORLA:advise</span>
    </div>

    <h1 class="holder-name">Tomas Vellaquin.</h1>
    <p class="holder-title">Managing Director</p>

    <p class="contact contact-tel">TEL: +6284729156048.</p>
    <p class="contact contact-email">EMAIL: tv@vorlaadvise.example</p>
    <p class="contact contact-web">WEBSITE: www.vorlaadvise.example</p>
  </main>
</body>
</html>
```